Kessel Fahrwerkstatt
Sehr angenehme zusammenarbeit nicht aufdringlich und genau auf die Wünsche eingegangen. Wir werde sicher noch mehr zusammen Arbeiten. Gruss Lukas Hemmerle Inhaber Kessel Fahrwerkstatt
Zielgruppe
Dinks und Kunden mit viel Erfolg und hohem Ausgabepotential.
Aufgabenstellung
Unsere Firma vertreibt Fahrzeuge im Luxusbereich hauptgebiet Valtro aber auch andere Sportwagen. Was uns fehlt ist ein optischer Wiedererkennugswert. Deshalb hätten wir gerne ein Visitenkarten Design und Briefpapier Design. Später soll auch noch eine Webseite mit gleichem Wiedererkennungswert entstehen. " Roter Faden "

```html
<!DOCTYPE html>
<html lang="de">
<head>
<meta charset="utf-8">
<title>Kessel Fahrwerkstatt – Geschäftsausstattung</title>
<link href="https://fonts.googleapis.com/css2?family=Open+Sans:wght@300;400;600&display=swap" rel="stylesheet">
<style>
  :root {
    --navy: #141f4a;
    --navy-deep: #0c1433;
    --navy-light: #25336b;
    --ink: #2b2b2b;
    --grey: #6d6d6d;
    --paper: #ffffff;
    --backdrop: #e9e7e3;
    --footer-text: #9aa3c4;
  }
  * { margin: 0; padding: 0; box-sizing: border-box; }
  html, body { width: 1200px; height: 800px; overflow: hidden; }
  body {
    background: var(--backdrop);
    font-family: "Open Sans", sans-serif;
    color: var(--ink);
    position: relative;
  }

  /* Visitenkarte */
  .card {
    position: absolute;
    left: 237px;
    width: 212px;
    height: 122px;
    box-shadow: 0 2px 6px rgba(0,0,0,.25);
    overflow: hidden;
  }
  .card--back {
    top: 334px;
    background: radial-gradient(circle at 30% 35%, var(--navy-light), var(--navy-deep) 80%);
    display: flex; align-items: center; justify-content: center;
  }
  .card--back .wordmark { color: #3d4c86; font-size: 11px; }
  .card--front {
    top: 490px;
    background: var(--paper);
  }
  .card--front .wordmark-wrap {
    position: absolute; top: 30px; left: 0; right: 0;
    display: flex; justify-content: center; align-items: center; gap: 6px;
  }
  .card__strip {
    position: absolute; left: 0; right: 0; bottom: 0; height: 36px;
    background: linear-gradient(90deg, var(--navy), var(--navy-light));
    padding: 6px 8px;
    color: var(--footer-text);
    font-size: 4.6px; line-height: 1.5;
  }

  .wordmark {
    font-weight: 300;
    letter-spacing: .12em;
    text-transform: uppercase;
    color: var(--ink);
    white-space: nowrap;
  }
  .mark-dot {
    width: 14px; height: 14px; border-radius: 50%;
    background: var(--ink);
    flex: none;
  }

  /* Briefbogen */
  .letter {
    position: absolute;
    left: 512px; top: 38px;
    width: 520px; height: 740px;
    background: var(--paper);
    border-top: 3px solid var(--navy);
    box-shadow: 0 3px 10px rgba(0,0,0,.25);
    font-size: 6.4px;
    line-height: 1.55;
  }
  .letter__logo {
    position: absolute; top: 52px; right: 56px;
    display: flex; align-items: center; gap: 8px;
  }
  .letter__logo .mark-dot { width: 26px; height: 26px; }
  .letter__logo .wordmark { font-size: 13px; }

  .recipient {
    position: absolute; top: 158px; left: 64px;
    font-weight: 600; font-size: 6.6px;
  }
  .sender {
    position: absolute; top: 158px; left: 364px;
    color: var(--grey);
  }
  .sender strong { color: var(--ink); font-weight: 600; }
  .sender p + p { margin-top: 8px; }

  .letter__body {
    position: absolute; top: 310px; left: 64px; width: 370px;
    color: var(--grey);
  }
  .letter__body p { margin-bottom: 10px; }
  .signature {
    width: 70px; height: 30px; margin-top: 6px;
    background: linear-gradient(90deg, rgba(30,50,180,.0), rgba(30,50,180,.35), rgba(30,50,180,.0));
    border-radius: 50%;
  }

  .letter__footer {
    position: absolute; left: 0; right: 0; bottom: 0; height: 80px;
    background: linear-gradient(90deg, var(--navy), var(--navy-light));
    color: var(--footer-text);
    font-size: 5.6px; line-height: 1.6;
    display: flex;
  }
  .footer__contact { padding: 22px 0 0 18px; width: 284px; }
  .footer__bank {
    margin-top: 10px; padding: 12px 0 0 12px;
    border-left: 1px solid #4a5787; height: 50px;
  }
</style>
</head>
<body>

  <section class="card card--back" aria-label="Visitenkarte Rückseite">
    <span class="wordmark">Kessel Fahrwerkstatt</span>
  </section>

  <section class="card card--front" aria-label="Visitenkarte Vorderseite">
    <div class="wordmark-wrap">
      <span class="mark-dot"></span>
      <span class="wordmark" style="font-size:9px">Kessel Fahrwerkstatt</span>
    </div>
    <div class="card__strip">
      Helga Andermatt | Geschäftsführerin<br>
      Lindenweg 12 | 73312 Talheim | Tel. +49 (0)7141 552310<br>
      Mobil +49 (0)171 4408823 | Fax +49 (0)7141 552311 | info@kessel-fahrwerk.de
    </div>
  </section>

  <article class="letter" aria-label="Briefbogen">
    <header class="letter__logo">
      <span class="mark-dot"></span>
      <span class="wordmark">Kessel Fahrwerkstatt</span>
    </header>

    <address class="recipient" style="font-style:normal">
      Max Mustermann<br>Musterstr. 1<br>12345 Muster
    </address>

    <address class="sender" style="font-style:normal">
      <p><strong>Helga Andermatt<br>Geschäftsführerin</strong></p>
      <p>Lindenweg 12<br>73312 Talheim</p>
      <p>Tel. +49 (0)7141 552310<br>Mobil +49 (0)171 4408823<br>Fax +49 (0)7141 552311<br>E-Mail: info@kessel-fahrwerk.de</p>
    </address>

    <div class="letter__body">
      <p>Sehr geehrte Damen und Herren,</p>
      <p>auch gibt es niemanden, der den Schmerz an sich liebt, sucht oder wünscht, nur weil er Schmerz ist, es sei denn, es kommt zu zufälligen Umständen, in denen Mühen und Schmerz ihm große Freude bereiten können.</p>
      <p>Um ein triviales Beispiel zu nehmen, wer von uns unterzieht sich je anstrengender körperlicher Betätigung, außer um Vorteile daraus zu ziehen? Aber wer hat irgend ein Recht, einen Menschen zu tadeln, der die Entscheidung trifft, eine Freude zu genießen, die keine unangenehmen Folgen hat, oder einen, der Schmerz vermeidet, welcher keine daraus resultierende Freude nach sich zieht? Auch gibt es niemanden, der den Schmerz an sich liebt, sucht oder wünscht, nur, weil er Schmerz ist, es sei denn, es kommt zu zufälligen Umständen, in denen Mühen und Schmerz ihm große Freude bereiten können.</p>
      <p>Um ein triviales Beispiel zu nehmen, wer von uns unterzieht sich je anstrengender körperlicher Betätigung, außer um Vorteile daraus zu ziehen? Aber wer hat irgend ein Recht, einen Menschen zu tadeln, der die Entscheidung trifft, eine Freude zu genießen, die keine unangenehmen Folgen hat, oder einen, der Schmerz vermeidet, welcher keine daraus resultierende Freude nach sich zieht?<br>Auch gibt es niemanden, der den Schmerz an sich liebt, sucht oder wünscht.</p>
      <p style="margin-top:18px;margin-bottom:0">Mit freundlichen Grüßen</p>
      <div class="signature" role="img" aria-label="Handschriftliche Unterschrift"></div>
    </div>

    <footer class="letter__footer">
      <div class="footer__contact">
        Helga Andermatt | Geschäftsführerin<br>
        Lindenweg 12 | 73312 Talheim | Tel. +49 (0)7141 552310<br>
        Mobil +49 (0)171 4408823 | Fax +49 (0)7141 552311 | E-Mail: info@kessel-fahrwerk.de
      </div>
      <div class="footer__bank">
        Bankverbindung: Kreisbank Talheim<br>
        Konto-Nr. 0 118 640 27 | BLZ 600 500 10
      </div>
    </footer>
  </article>

</body>
</html>
```